Global Nano Technology Surface Protection company needs a new logo and cards

We are a Global company that will apply nanotechnology coatings on surfaces to prevent growth and spread of bacteria, viruses, mold etc. We deal with large corporates, airlines, hospitals and schools so we are after a new modern, simple and clean look that will have great visual impact.
We a company that is focused on prevention and protection.

Company name, Luminary Fabrications Worldwide

Subtext, Antimicrobial Surface Protection

Logo, LFWW or LFW

Target Market(s)

Hospitals, Transport agencies, Airlines, Corporate entities

Industry/Entity Type

Protection

Contact Information for Business Card

Logo, LFWW or LFW
www.lfww.us
Derek Hawtrey
+64213958260
tidyshieldnz@mailbox.example

Logo Text

LFWW

Requirements
Must have
• Simple clean look
Should not have
• Nothing too messy

```html
<!DOCTYPE html>
<html lang="en">
<head>
<meta charset="utf-8">
<title>Luminary Fabrications Worldwide — Business Cards</title>
<link href="https://fonts.googleapis.com/css2?family=Source+Sans+3:wght@300;400;600;700&display=swap" rel="stylesheet">
<style>
  :root {
    --backdrop: #dddddd;
    --card-light: #e9edef;
    --brand-navy: #01486b;
    --brand-mark-soft: #d6dde2;
    --brand-mark-deep: #0b5f8c;
  }
  * { margin: 0; padding: 0; box-sizing: border-box; }
  html, body {
    width: 1200px; height: 1200px; overflow: hidden;
    background: var(--backdrop);
    font-family: "Source Sans 3", sans-serif;
    color: var(--brand-navy);
  }
  .canvas { position: relative; width: 1200px; height: 1200px; }

  .brand-wordmark {
    position: absolute; left: 34px; top: 14px;
    font-weight: 700; font-size: 142px; line-height: 1;
    letter-spacing: -2px; color: var(--brand-navy);
  }

  .card {
    position: absolute; width: 516px; height: 296px;
  }
  .card-back {
    left: 517px; top: 548px; z-index: 1;
    background: var(--brand-navy);
    display: flex; align-items: center; justify-content: center;
  }
  .card-back .card-mark {
    font-weight: 700; font-size: 50px; line-height: 1;
    color: var(--brand-mark-deep); letter-spacing: -0.5px;
    transform: translateY(-4px);
  }
  .card-front {
    left: 160px; top: 317px; z-index: 2;
    background: var(--card-light);
  }
  .card-front .card-mark {
    position: absolute; left: 8px; top: 6px;
    font-weight: 700; font-size: 46px; line-height: 1;
    color: var(--brand-mark-soft); letter-spacing: -0.5px;
  }
  .holder-name {
    position: absolute; left: 230px; top: 91px;
    font-weight: 600; font-size: 31px; line-height: 1;
  }
  .contact-list {
    position: absolute; left: 36px; top: 183px;
    list-style: none; font-weight: 300; font-size: 16px;
  }
  .contact-list li {
    display: flex; align-items: center; height: 25px;
  }
  .contact-list svg { width: 20px; height: 16px; margin-right: 6px; flex: none; }
  .company-block {
    position: absolute; left: 36px; top: 252px; line-height: 1.1;
  }
  .company-name { font-weight: 700; font-size: 12.5px; letter-spacing: 0.3px; }
  .company-tagline { font-weight: 400; font-size: 9.5px; letter-spacing: 0.3px; }
  .web-address {
    position: absolute; right: 6px; bottom: 11px;
    writing-mode: vertical-rl; transform: rotate(180deg);
    font-weight: 700; font-size: 12.5px; line-height: 1;
    letter-spacing: 0.8px; white-space: nowrap;
  }
</style>
</head>
<body>
<main class="canvas">
  <div class="brand-wordmark">LFWW</div>

  <section class="card card-back">
    <div class="card-mark">LFWW</div>
  </section>

  <section class="card card-front">
    <div class="card-mark">LFWW</div>
    <h1 class="holder-name">Derek Hawtrey</h1>
    <ul class="contact-list">
      <li>
        <svg viewBox="0 0 20 16" aria-hidden="true">
          <path d="M3 1.5c1-.8 2-.6 2.6.3l1.6 2.4c.5.8.3 1.6-.4 2.1l-1 .7c.9 2 2.4 3.6 4.4 4.6l.8-1c.5-.7 1.4-.8 2.1-.3l2.3 1.7c.8.6.9 1.6.1 2.5-1 1.2-2.4 1.6-4 1C6.8 13.9 3.3 10.2 2 5.8 1.6 4.2 2 2.5 3 1.5z" fill="var(--brand-navy)"/>
        </svg>
        +64213958260
      </li>
      <li>
        <svg viewBox="0 0 20 16" aria-hidden="true">
          <rect x="0.8" y="1.3" width="18.4" height="13.4" fill="none" stroke="var(--brand-navy)" stroke-width="1.1"/>
          <path d="M1 1.6l9 7 9-7M1 14.4l6.5-6M19 14.4l-6.5-6" fill="none" stroke="var(--brand-navy)" stroke-width="1.1"/>
        </svg>
        tidyshieldnz@mailbox.example
      </li>
    </ul>
    <div class="company-block">
      <div class="company-name">Luminary Fabrications Worldwide</div>
      <div class="company-tagline">Antimicrobial Surface Protection</div>
    </div>
    <div class="web-address">www.lfww.us</div>
  </section>
</main>
</body>
</html>
```